Wordpress design for my private practice website - Psychotherapist

I would like a simple, clean, and elegant design for my private practice website. I work with both adults and children so I'd like it to appeal to both. However, since parents make the choice as to where to send their child for therapy, I want it to appeal to adults more. I would like the pictures on the site to have a calming effect - maybe using sand and water and rocks. I am attaching files with my company logo. I would also like my name incorporated into the header - Colette Brannigan, LCSW, Registered Play Therapist. I've also uploaded a picture of myself for my About Page.

I like the design of these 2 website and want something similar:
www.drlorapenwick.example
www.harwood-tallis.example

I would like a home page that highlights a calming graphic across the entire top of the page as well as my practice logo and my name.

I'd like a link to social media sites on the top of the homepage - facebook, pinterest.

I want a simple bar across the top with the following tabs:
Home
About Me (subtabs Who I Am, Specialties and Approach)
Counseling Services (subtabs Individual Counseling, Play Therapy, Sandplay Therapy,)
Fees
FAQs
Contact Me (would love this to be a fill in the blank contact form that sends info to my email address - should include name, phone number, email and a comment box for more information requested)
Blog (this will link with another wordpress blog)

Target Market(s)

Parents of children under age 12 with behavioral problems or are dealing with the breakup of their family through divorce - looking for someone to work with their young child. I also work with Adults that are overwhelmed and worried - often women that have many life stressors and are feeling burnt out on life and meeting everyone's needs. Families going through some type of trauma, including divorce or grief work. I also work with individuals going through a transition of religious beliefs - often exiting the religion of their youth and undergoing a crisis of faith at midlife.

Industry/Entity Type

Mental Health

Contact Information for Business Card

Colette Brannigan, LCSW
Registered Play Therapist
4917 Wexmoor Lane
Idaho Falls, Idaho 83404
(208)555-0187
www.stillbrookcounseling.example

On the opposite side, I'd like an appointment reminder area - with the following text:

Your next appointment is
_____/______/______ at ______am/pm
Please give 24 hrs notice if you need to cancel your appointment.

Coding

Coded - Design and coding required

Number of Pages Required

5+ page

Font styles to use
Sans Serif

Colors
33a6d7
9bcb3c
0355a3

Requirements
Must have
• I'd like it to be a wordpress site. I'm such a newby at web design - but I need to be able to add content and manage the site myself once it is up and running.
Nice to have
• I like the design of these 2 websites and want something similar:
• www.drlorapenwick.example
• www.harwood-tallis.example
• They are clean, easy to navigate and calming.
Should not have
• Should not look like a childcare website.

```html
<!DOCTYPE html>
<html lang="en">
<head>
<meta charset="utf-8">
<title>Stillbrook Counseling – Home</title>
<link rel="stylesheet" href="https://fonts.googleapis.com/css2?family=Arimo:ital,wght@0,400;0,700;1,400&family=Old+Standard+TT:wght@400;700&family=Raleway:wght@300&display=swap">
<style>
  :root {
    --page-bg: #f1f1f1;
    --white: #ffffff;
    --text: #555a60;
    --text-soft: #777b80;
    --rule: #dcdcdc;
    --nav-active: #c9a15a;
    --nav-text: #333638;
    --cta-blue: #22568a;
    --accent-green: #7f9d2b;
    --footer-teal: #24728f;
    --footer-base: #1f4e7b;
    --tab-bg: #e6e6e6;
    --tab-border: #d4d4d4;
    --serif: "Old Standard TT", Georgia, serif;
    --sans: "Arimo", Arial, sans-serif;
  }
  * { box-sizing: border-box; margin: 0; padding: 0; }
  html, body { width: 846px; height: 1200px; overflow: hidden; }
  body { background: var(--page-bg); font-family: var(--sans); color: var(--text); position: relative; }

  /* Header */
  .hero {
    position: absolute; left: 6px; top: 6px; width: 835px; height: 150px;
    background: linear-gradient(180deg, #b89a7a 0%, #8fa2ad 22%, #5f7f8e 42%, #cfc5b5 55%, #b79c7f 75%, #8a735c 100%);
  }
  .hero-stones {
    position: absolute; right: 150px; top: 0; width: 120px; height: 150px;
    background: radial-gradient(ellipse at 50% 60%, #9a8474 0%, #7d6a5c 45%, rgba(125,106,92,0) 72%);
  }
  .brand {
    position: absolute; left: 132px; top: 90px; width: 190px;
    font-family: "Raleway", Arial, sans-serif; font-weight: 300; color: var(--white);
    font-size: 13px; letter-spacing: 3px; text-transform: uppercase; text-align: center; line-height: 16px;
  }
  .site-nav {
    position: absolute; left: 6px; top: 156px; width: 835px; height: 26px;
    background: var(--white); box-shadow: 0 3px 4px rgba(0,0,0,.15);
    display: flex; justify-content: center; align-items: center; gap: 11px;
  }
  .site-nav a { font-size: 7.5px; text-transform: uppercase; letter-spacing: .6px; color: var(--nav-text); text-decoration: none; }
  .site-nav a.is-active { color: var(--nav-active); }

  .rule { position: absolute; left: 138px; width: 574px; height: 1px; background: var(--rule); }

  /* Intro */
  .intro-photo { position: absolute; left: 138px; top: 233px; width: 181px; height: 210px;
    background: linear-gradient(180deg, #c9d9e4 0%, #dfe6e8 45%, #b8aa95 70%, #6f6758 100%); }
  .intro-text { position: absolute; left: 334px; top: 242px; width: 378px; font-size: 7px; line-height: 10.9px; }
  .intro-text p { margin-bottom: 10px; }
  .float-spacer { float: right; width: 0; height: 21px; }
  .portrait { float: right; clear: right; width: 98px; height: 150px; margin: 0 0 4px 8px; background: var(--white); }
  .portrait-photo { width: 98px; height: 141px; background: linear-gradient(180deg, #9fb36a 0%, #e2c28f 40%, #3e5a3a 100%); position: relative; }
  .portrait-name { position: absolute; left: 6px; bottom: 8px; right: 6px; background: var(--cta-blue); color: var(--white);
    font-family: var(--serif); font-size: 7px; text-align: center; padding: 2px 0; }
  .portrait-caption { font-size: 4px; text-align: center; color: #333; line-height: 9px; }

  /* Call to action */
  .cta { position: absolute; left: 135px; top: 494px; width: 573px; height: 55px; background: var(--cta-blue);
    border-bottom: 3px solid var(--accent-green); border-radius: 2px;
    display: flex; align-items: center; justify-content: center;
    font-family: var(--serif); color: var(--white); font-size: 14px; }

  /* Tabs */
  .tabs { position: absolute; left: 140px; top: 589px; display: flex; }
  .tab { height: 27px; padding: 0 9px; display: flex; align-items: center; font-size: 7px; color: var(--text);
    background: var(--tab-bg); border: 1px solid var(--tab-border); border-left: none; }
  .tab:first-child { border-left: 1px solid var(--tab-border); }
  .tab.is-active { background: var(--white); border-bottom-color: var(--white); }
  .tab-panel { position: absolute; left: 140px; top: 615px; width: 572px; height: 126px; background: var(--white); }
  .tab-photo { position: absolute; left: 10px; top: 16px; width: 123px; height: 103px;
    background: linear-gradient(135deg, #f3f1ec 0%, #d9d2c8 55%, #8d8a86 100%); }
  .tab-text { position: absolute; left: 144px; top: 16px; width: 418px; font-size: 7px; line-height: 10.9px; }
  .tab-text p { margin-bottom: 9px; }

  /* Testimonials */
  .testimonials { position: absolute; left: 5px; top: 750px; width: 836px; height: 256px;
    background: linear-gradient(180deg, #e5a761 0%, #f3a53c 22%, #c9805a 38%, #7d8aa0 52%, #5b5c63 70%, #2f3238 100%); }
  .testimonials h2 { position: absolute; left: 0; right: 0; top: 40px; text-align: center; font-family: var(--serif);
    font-weight: 400; color: var(--white); font-size: 14px; }
  .testimonials .band-rule { position: absolute; left: 133px; width: 574px; top: 78px; height: 1px; background: rgba(255,255,255,.45); }
  .quote-card { position: absolute; left: 161px; top: 96px; width: 515px; height: 142px;
    background: linear-gradient(180deg, #ffffff 0%, #ececec 100%); padding: 14px 12px 0 12px; }
  .quote-title { display: flex; align-items: center; gap: 6px; font-family: var(--serif); font-weight: 700; font-size: 9px; color: #333; }
  .quote-body { margin-top: 10px; font-style: italic; font-size: 7px; line-height: 10.9px; color: #666; }
  .quote-body p { margin-bottom: 8px; }
  .quote-author { text-align: right; font-size: 7px; font-weight: 700; color: #333; }

  /* Footer */
  .site-footer { position: absolute; left: 5px; top: 1018px; width: 836px; height: 139px; background: var(--footer-teal); color: var(--white); }
  .footer-col { position: absolute; top: 8px; width: 172px; font-size: 7px; line-height: 9px; }
  .footer-col h3 { font-family: var(--serif); font-weight: 400; font-size: 12px; margin-bottom: 9px; }
  .footer-col ul { list-style: none; }
  .posts li { padding: 2px 0 3px; border-bottom: 1px solid rgba(255,255,255,.45); margin-bottom: 3px; }
  .posts li:last-child { border-bottom: none; }
  .footer-band { position: absolute; left: 5px; top: 1157px; width: 836px; height: 6px; background: var(--accent-green); }
  .footer-base { position: absolute; left: 5px; top: 1163px; width: 836px; height: 30px; background: var(--footer-base);
    font-size: 5.5px; color: #c9d4df; display: flex; align-items: center; justify-content: center; }
  .to-top { position: absolute; left: 811px; top: 1162px; }
</style>
</head>
<body>

<header>
  <div class="hero" role="img" aria-label="Beach photograph of sand, sea and a stack of smooth stones">
    <div class="hero-stones"></div>
  </div>
  <div class="brand">Stillbrook Counseling</div>
  <nav class="site-nav">
    <a class="is-active" href="#">Home</a>
    <a href="#">About Colette</a>
    <a href="#">Counseling Services</a>
    <a href="#">Fees</a>
    <a href="#">FAQ's</a>
    <a href="#">Testimonials</a>
    <a href="#">Latest News</a>
    <a href="#">Contact</a>
  </nav>
</header>

<main>
  <div class="rule" style="top:214px"></div>

  <section class="intro">
    <div class="intro-photo" role="img" aria-label="Photograph of a couple playing on rocks at the beach"></div>
    <div class="intro-text">
      <div class="float-spacer"></div>
      <figure class="portrait">
        <div class="portrait-photo" role="img" aria-label="Portrait photograph of Colette Brannigan">
          <div class="portrait-name">Colette Brannigan</div>
        </div>
        <figcaption class="portrait-caption">LCSW, Registered Play Therapist</figcaption>
      </figure>
      <p>Colette Brannigan, LCSW, Registered Play Therapist is a licensed psychologist specializing in counseling for parents of children under age 12 with behavioral problems or are dealing with the breakup of their family through divorce – looking for someone to work with their young child. I also work with Adults that are overwhelmed and worried – often women that have many life stressors and are feeling burnt out on life and meeting everyone's needs. Families going through some type of trauma, including divorce or grief work. I also work with individuals going through a transition of religious beliefs – often exiting the religion of their youth and undergoing a crisis of faith at midlife.</p>
      <p>Qui iusto recteque ne, euismod nostrum ne per. Euismod appetere urbanitas eos ea, eu alia singulis ius, dico fugit alterum te sea. Usu omnes mediocrem similique id. Nibh altera dignissim cu his, ea mel alterum aliquid disputando. Pro id dicant oblique posidonium, nam ad quot definitiones, vel ea esse ipsum aliquip. Est civibus detracto iudicabit ad.</p>
      <p>An verear propriae conclusionemque mel, at libris salutatus vis. Vocibus legendos eam ad. Movet inimicus an sea, populo gubergren tincidunt quo ut. Deterruisset definitionem ex sea. Vide senserit at nam, te dolore oportere intellegam pri. At quaestio explicari argumentum est.</p>
    </div>
  </section>

  <a class="cta" href="#">Contact Colette Brannigan on 0400 555 0100 to book an appointment today</a>

  <div class="rule" style="top:571px"></div>

  <section class="services">
    <div class="tabs">
      <div class="tab is-active">Marital Problems</div>
      <div class="tab">Play Therapy</div>
      <div class="tab">Sand Play Therapy</div>
      <div class="tab">Family Behavioral Problems</div>
      <div class="tab">Grief Counseling</div>
      <div class="tab">Youth Counseling</div>
    </div>
    <div class="tab-panel">
      <div class="tab-photo" role="img" aria-label="Photograph of a distressed couple on a sofa"></div>
      <div class="tab-text">
        <p>Lorem ipsum dolor sit amet, vivendo fabellas reprehendunt in est. Commodo ornatus gloriatur et qui, partem gloriatur referrentur in mel, quo ex eros probo. Te quo semper eirmod philosophia. Cum integre honestatis eu. Ut nullam tempor vis, eum fuisset intellegam te. Mollis discere ne sea. Salutatus appellantur vix ut.</p>
        <p>Qui iusto recteque ne, euismod nostrum ne per. Euismod appetere urbanitas eos ea, eu alia singulis ius, dico fugit alterum te sea. Usu omnes mediocrem similique id. Nibh altera dignissim cu his, ea mel alterum aliquid disputando. Pro id dicant oblique posidonium, nam ad quot definitiones, vel ea esse ipsum aliquip. Est civibus detracto iudicabit ad.</p>
      </div>
    </div>
  </section>

  <section class="testimonials" role="img" aria-label="Photograph of a sunset over a rocky beach">
    <h2>Testimonials</h2>
    <div class="band-rule"></div>
    <blockquote class="quote-card">
      <div class="quote-title">
        <svg width="15" height="11" viewBox="0 0 15 11" aria-hidden="true"><g fill="#888"><circle cx="3.2" cy="7.5" r="3.2"/><path d="M0.4 7 Q0.8 1.5 5.5 0.3 L5.8 1.3 Q2.6 2.6 2.5 6 Z"/><circle cx="10.7" cy="7.5" r="3.2"/><path d="M7.9 7 Q8.3 1.5 13 0.3 L13.3 1.3 Q10.1 2.6 10 6 Z"/></g></svg>
        Extremely Professional
      </div>
      <div class="quote-body">
        <p>Lorem ipsum dolor sit amet, vivendo fabellas reprehendunt in est. Commodo ornatus gloriatur et qui, partem gloriatur referrentur in mel, quo ex eros probo. Te quo semper eirmod philosophia. Cum integre honestatis eu. Ut nullam tempor vis, eum fuisset intellegam te. Mollis discere ne sea. Salutatus appellantur vix ut.</p>
        <p>Qui iusto recteque ne, euismod nostrum ne per. Euismod appetere urbanitas eos ea, eu alia singulis ius, dico fugit alterum te sea. Usu omnes mediocrem similique id. Nibh altera dignissim cu his, ea mel alterum aliquid disputando. Pro id dicant oblique posidonium, nam ad quot definitiones, vel ea esse ipsum aliquip. Est civibus detracto iudicabit ad.</p>
      </div>
      <div class="quote-author">Ruth Adler</div>
    </blockquote>
  </section>
</main>

<footer>
  <div class="site-footer">
    <div class="footer-col" style="left:132px">
      <h3>Contact Information</h3>
      <p>Colette Brannigan<br>LCSW<br>Registered Play Therapist<br>27 Harbour Road<br>Eastvale US 10090</p>
      <p style="margin-top:9px">Tel: 054 555 0142<br>Mobile: 0400 555 010<br>Email: colette@stillbrook.example</p>
    </div>
    <div class="footer-col posts" style="left:333px">
      <h3>Recent Posts</h3>
      <ul>
        <li>Post with custom slideshow</li>
        <li>Just video post</li>
        <li>Ut tincidunt imperdiet</li>
        <li>Quote Post</li>
        <li>Audio Post</li>
      </ul>
    </div>
    <div class="footer-col" style="left:534px">
      <h3>Additional Pages</h3>
      <ul>
        <li>Counseling Services</li>
        <li>Children's Counseling Services</li>
        <li>Play Therapy</li>
        <li>Sand Play Therapy</li>
        <li>FAQ's</li>
        <li>Contact Details</li>
        <li>Privacy Disclaimer</li>
        <li>Terms &amp; Conditions</li>
      </ul>
    </div>
  </div>
  <div class="footer-band"></div>
  <div class="footer-base">Copyright © 2016 Colette Brannigan. All rights reserved.</div>
  <svg class="to-top" width="20" height="20" viewBox="0 0 20 20" aria-label="Back to top" role="img">
    <circle cx="10" cy="10" r="10" fill="#0b0b0b"/>
    <path d="M6.5 11.8 L10 8.3 L13.5 11.8" fill="none" stroke="#fff" stroke-width="1.6"/>
  </svg>
</footer>

</body>
</html>
```